Registry Program Flyer design 2 - MX Bridge registry

We need two different flyers that will be distributed via web, email and print. This project is for the second of the two flyers.

The audience is patients and family members of patients with a specific disease. The flyer will be used to make patients aware of our web-based registry programs, and to inform/encourage patients to join.

An example prototype flyer with the text that should be used is attached. We would like to improve the design and layout of the flyer, while retaining as much of the language as appropriate.

The MXBridge flyer should use the logo provided in the example and a color scheme compatible with the logo. The flyer may use the pictures included in the prototype.

If possible, a final format that allows us to edit the text is preferred. If this is not possible, we will finalize the text after receiving a prototype. Changes to the text will likely be minor.

Note: The design of the flyers for this project and the other project (Registry Program Flyer Design 1 - RTQV registry) can be similar in style, however, they should not be duplicates.

Deliverables will be a final .PSD (photoshop) file with layers so we can edit text if necessary.

Target Market(s)

Physicians and healthcare professionals.

Requirements
Must have
• Use the attached logo and colors.

```html
<!DOCTYPE html>
<html lang="en">
<head>
<meta charset="utf-8">
<title>MX Bridge Registry Flyer</title>
<link href="https://fonts.googleapis.com/css2?family=Oswald:wght@700&family=Roboto+Condensed:wght@400;700&display=swap" rel="stylesheet">
<style>
  :root {
    --stage: #e9e9e9;
    --paper: #ffffff;
    --brand-red: #e0262b;
    --deep-red: #c81c22;
    --ink: #1e1e1e;
    --body-ink: #3a3a3a;
    --highlight: #ffe14a;
    --tagline: #3d4f9e;
    --sky: #a9cde8;
    --leaf: #9cc45a;
  }
  * { box-sizing: border-box; margin: 0; padding: 0; }
  html, body { width: 900px; height: 1200px; overflow: hidden; background: var(--stage); }
  body { font-family: "Roboto Condensed", Arial, sans-serif; }

  .flyer {
    position: absolute; left: 60px; top: 80px;
    width: 780px; height: 1040px;
    background: var(--paper);
    overflow: hidden;
    box-shadow: 0 6px 24px rgba(0,0,0,.18);
  }
  .hero-photo {
    position: absolute; left: 0; top: 0; width: 780px; height: 430px;
    background:
      radial-gradient(ellipse at 30% 60%, #d8473f 0 18%, transparent 34%),
      linear-gradient(160deg, var(--sky) 0%, #d7ecc0 40%, var(--leaf) 70%, #ffffff 100%);
  }
  .hero-fade {
    position: absolute; left: 0; top: 300px; width: 780px; height: 130px;
    background: linear-gradient(to bottom, rgba(255,255,255,0), var(--paper));
  }

  .intro { position: absolute; left: 32px; top: 350px; width: 292px; }
  .intro-join {
    font-family: "Oswald", Impact, sans-serif; font-weight: 700;
    font-size: 78px; line-height: 1; color: var(--brand-red); letter-spacing: -1px;
  }
  .intro-url {
    font-weight: 700; font-size: 26px; color: var(--ink); line-height: 1.1; margin-top: 2px;
  }
  .intro-url span { color: var(--brand-red); }
  .intro-body {
    margin-top: 14px; font-size: 11.6px; line-height: 1.32; color: var(--body-ink); text-align: justify;
  }
  .intro-heading {
    margin-top: 12px; font-size: 13px; font-weight: 700; color: var(--brand-red);
  }
  .intro-list { list-style: none; font-size: 11.6px; line-height: 1.32; color: var(--body-ink); }
  .intro-list li::before { content: "- "; }
  .intro-close { font-size: 11.6px; line-height: 1.32; color: var(--body-ink); text-align: justify; }
  .tagline {
    margin-top: 12px; font-size: 16px; line-height: 1.2; color: var(--tagline);
  }
  .partners { display: flex; align-items: center; gap: 16px; margin-top: 14px; }
  .partner-name { font-size: 11px; font-weight: 700; color: var(--ink); line-height: 1.05; display: flex; align-items: center; gap: 4px; }
  .partner-name i { width: 10px; height: 10px; background: var(--brand-red); display: inline-block; }
  .partner-badge { width: 34px; height: 30px; border-radius: 50%; background: #cfd8ea; }
  .partner-badge.wide { width: 44px; border-radius: 6px; background: #bfe0f0; }
  .sponsor {
    margin-top: 14px; padding-top: 6px; border-top: 1px solid #bbb;
    font-size: 11px; color: var(--ink); display: flex; align-items: center; gap: 12px;
  }
  .sponsor-name { font-size: 15px; font-weight: 700; color: var(--deep-red); }

  .panel {
    position: absolute; left: 346px; top: 250px; width: 390px; height: 772px;
    background: var(--brand-red);
    box-shadow: -4px 4px 10px rgba(0,0,0,.2);
  }
  .panel-logo {
    height: 90px; background: var(--paper);
    display: flex; align-items: center; gap: 12px; padding-left: 24px;
    border: 1px solid #ddd;
  }
  .panel-logo i { width: 34px; height: 34px; background: var(--brand-red); display: block; }
  .panel-logo span { font-size: 34px; color: var(--ink); font-weight: 400; }
  .panel-content { padding: 12px 24px 0 24px; color: #fff; font-size: 12.6px; line-height: 1.3; }
  .panel-heading { color: var(--highlight); font-size: 13px; font-weight: 700; }
  .panel-list { list-style: none; font-weight: 700; margin-bottom: 2px; }
  .panel-list li::before { content: "\\ "; color: #fff; font-weight: 700; }
  .panel-text { text-align: justify; margin-bottom: 2px; }
  .panel-cta { margin-top: 12px; font-size: 14px; line-height: 1.25; }
  .panel-photos {
    position: absolute; left: 0; bottom: 42px; width: 390px; height: 150px;
    display: grid; grid-template-columns: 1fr 1fr; grid-template-rows: 1fr 1fr; gap: 2px;
    background: var(--paper);
  }
  .panel-photos div { background: linear-gradient(160deg, #8fb8d8, #6b9a4a); }
  .panel-photos div:nth-child(2) { background: linear-gradient(160deg, #a9c7e0, #7a9c5c); }
  .panel-photos div:nth-child(3) { background: linear-gradient(160deg, #8aa86a, #c9b24a); }
  .panel-photos div:nth-child(4) { background: linear-gradient(160deg, #6f9a52, #b7542f); }
</style>
</head>
<body>
<main class="flyer">
  <div class="hero-photo" role="img" aria-label="Photo of a woman in a red running top jogging outdoors under green trees and blue sky"></div>
  <div class="hero-fade"></div>

  <section class="intro">
    <div class="intro-join">Join</div>
    <div class="intro-url">mxbridge.org today<span>!</span></div>
    <p class="intro-body">One of the most important steps towards finding effective treatments for lipodystrophy (LD) is to uncover the ways in which the diseases behave, the symptoms that are commonly seen and how those symptoms progress. This requires the collection of as much information as possible about all people affected by LD. MX Bridge will serve as that database–the critical link between the patient community and the scientific community. The more people who join the registry the greater the chances that research will produce results that benefit everyone.</p>
    <h3 class="intro-heading">Join THE MX BRIDGE RTQV Registry to:</h3>
    <ul class="intro-list">
      <li>Tell us about your experience with LD and learn about the experiences with others</li>
      <li>Share information in a program that protects your privacy</li>
      <li>Provide valuable quality-of-life information that can be used to advocate on behalf of the LD community</li>
      <li>Help the research community launch clinical trials and studies</li>
    </ul>
    <p class="intro-close">We need to hear YOUR VOICE and we hope you will decide to join MX Bridge. Every individual who joins makes a vital contribution toward helping all of those affected by lipodystrophy.</p>
    <p class="tagline">Your information will lead to future treatments and cures for all types of Lipodystrophy</p>
    <div class="partners">
      <div class="partner-name"><i></i>Care Alliance<br>United</div>
      <div class="partner-badge wide"></div>
      <div class="partner-badge"></div>
      <div class="partner-badge"></div>
    </div>
    <div class="sponsor">Sponsored by : <span class="sponsor-name">Norvane Pharma</span></div>
  </section>

  <aside class="panel">
    <div class="panel-logo"><i></i><span>MX Bridge</span></div>
    <div class="panel-content">
      <h3 class="panel-heading">Who Can Participate</h3>
      <ul class="panel-list">
        <li>Patients</li>
        <li>Family members</li>
        <li>Healthcare providers</li>
        <li>Investigators &amp; researchers</li>
        <li>All stakeholders interested in RTQV</li>
      </ul>
      <h3 class="panel-heading">How it Works</h3>
      <p class="panel-text">Patients can join the registry to submit their data. After taking web-based surveys, explore the collected information in a way that protects the privacy of everyone.</p>
      <h3 class="panel-heading">Who We Are</h3>
      <p class="panel-text">As its name implies, MX Bridge represents the coming together of a wide range of entities and individuals who recognize the value in pooling their combined expertise and information. The Governing Board of MX Bridge comes from leaders in the non-profit sector, government agencies and academic institutions. Regardless of their individual backgrounds, the thought leaders of MX Bridge share a common goal to increase the community's ability to help one another through improved communication, and by doing so, to help the millions of people affected by Lipodystrophy.</p>
      <p class="panel-cta">Your information will lead to future treatments and cures for all types of Lipodystrophy</p>
    </div>
    <div class="panel-photos" role="img" aria-label="Collage of four photos of older adults and families jogging outdoors">
      <div></div><div></div><div></div><div></div>
    </div>
  </aside>
</main>
</body>
</html>
```